Overseas Property Tax Depreciation

We need a two sided flyer to promote our business and explain what we do. our website is www.tolbexmu.net.
The attached word file is what I would like on an A5 size flyer with one side showing the FAQ and the other the worked example. I would like these formatted much better than the are and in general style of the website. I will attach files for logos as well.

```html
<!DOCTYPE html>
<html lang="en">
<head>
<meta charset="utf-8">
<title>Tolbexmu Depreciation – Flyer</title>
<link href="https://fonts.googleapis.com/css2?family=Didact+Gothic&family=Arimo:wght@400;700&display=swap" rel="stylesheet">
<style>
:root{
  --orange:#f7a600;
  --orange-light:#fdd300;
  --green:#3f9b2e;
  --green-light:#8dc63f;
  --heading:#72b626;
  --text:#333;
  --cream:#fbf4ea;
  --bg:#f2f2f2;
  --rule:#9a9a9a;
}
*{box-sizing:border-box;margin:0;padding:0}
html,body{width:1200px;height:850px;overflow:hidden;background:var(--bg)}
body{position:relative;font-family:"Arimo",Arial,sans-serif;color:var(--text)}
.page{position:absolute;top:68px;width:518px;height:724px;background:linear-gradient(180deg,#fff 0%,#fff 45%,#fdf0df 100%);overflow:hidden}
.page--faq{left:90px}
.page--example{left:626px}
.band-top{position:absolute;left:0;top:30px;height:18px;background:var(--orange)}
.band-top-line{position:absolute;left:0;top:50px;height:7px;background:var(--green)}
.page--faq .band-top,.page--faq .band-top-line{width:352px}
.page--example .band-top{top:32px;width:364px;height:14px}
.page--example .band-top-line{top:48px;width:364px;height:8px}
.brand{position:absolute;display:flex;align-items:center;gap:6px;font-family:"Didact Gothic",sans-serif;color:var(--green);font-size:17px}
.brand-dot{width:12px;height:12px;border-radius:50%;background:var(--orange)}
.page--faq .brand{right:22px;top:30px}
.page--example .brand{right:22px;bottom:18px;color:#fff}
.band-bottom{position:absolute;left:0;right:0;bottom:0;height:60px;background:linear-gradient(90deg,var(--green),var(--green-light))}
.partner{position:absolute;left:28px;bottom:18px;font-family:"Didact Gothic",sans-serif;color:#fff;font-size:20px;display:flex;align-items:center;gap:8px}
.partner-mark{width:22px;height:22px;border-radius:50%;background:#fff}
.badge{position:absolute;right:22px;bottom:6px;width:44px;height:58px;background:#fff}
.card{position:absolute;background:var(--cream);box-shadow:1px 2px 4px rgba(0,0,0,.18);padding:4px 6px;font-size:8.6px;line-height:1.2}
.card h2{font-family:"Didact Gothic",sans-serif;font-weight:400;color:var(--heading);font-size:16px;line-height:1.05;text-align:center;margin-bottom:3px}
.card p{text-align:justify}
.ticks{list-style:none}
.ticks li{padding-left:12px;position:relative;text-align:justify}
.ticks li::before{content:"";position:absolute;left:1px;top:1px;width:4px;height:7px;border:solid var(--green-light);border-width:0 2px 2px 0;transform:rotate(40deg)}
.example-title{position:absolute;right:8px;top:30px;text-align:right;font-family:"Didact Gothic",sans-serif;color:var(--heading);font-size:8.6px;line-height:1.25}
.sheet{position:absolute;left:22px;top:122px;width:466px;border:3px solid var(--rule);background:#fff}
table{border-collapse:collapse;width:460px;font-size:9px;table-layout:fixed}
col.c-ref{width:28px}
col.c-desc{width:162px}
col.c-note{width:96px}
col.c-eur{width:50px}
col.c-aud{width:50px}
col.c-with{width:74px}
td,th{font-weight:400;padding:1px 3px;vertical-align:middle;height:17px;overflow:hidden}
th{text-align:left}
.ref{text-align:center;border-right:1px solid #ccc}
.note{padding-left:0;white-space:nowrap;font-size:8.6px}
.eur,.aud{text-align:left;white-space:nowrap;background:linear-gradient(90deg,var(--orange),var(--orange-light));border-left:1px solid #fff}
.with{text-align:right;white-space:nowrap;padding-right:6px;background:linear-gradient(90deg,var(--green),var(--green-light));border-left:3px solid var(--rule)}
thead th.eur,thead th.aud,thead th.with{text-align:center;font-size:8px;line-height:1.1;white-space:normal}
thead tr:last-child th{border-bottom:1px solid #fff}
.group td{border-top:3px solid var(--rule)}
.sub td{border-top:1px solid #bbb}
.green-text{color:var(--green)}
.green-text td.eur,.green-text td.aud{color:#3c8c1f}
.with.green-val{color:#fff}
</style>
</head>
<body>

<section class="page page--faq">
  <div class="band-top"></div>
  <div class="band-top-line"></div>
  <div class="brand"><span class="brand-dot"></span>Tolbexmu Depreciation</div>

  <article class="card" style="left:22px;top:82px;width:326px;height:305px">
    <h2>Why use us?</h2>
    <p>There are several websites out there offering tax depreciation reports for Australian properties but there are very few who are appropriately qualified and approved by the Australian Tax Office (ATO) and offer the necessary Irish expertise. The Quantity Surveyor that prepares your report:</p>
    <ul class="ticks">
      <li>is Irish and qualified as a Quantity Surveyor in Ireland.</li>
      <li>worked there during the "Celtic Tiger" period when construction costs were quite high.</li>
      <li>has detailed knowledge of Irish construction methods and costs over the past 20 years. Irish buildings are generally much more expensive than Australia due to the climate, just think about how many Australian houses you have seen that have double glazing, central heating, insulation etc..</li>
      <li>has a partnership arrangement with an Irish quantity surveying firm to carry out the property inspections required in most cases to maximize the deductions available.</li>
      <li>is a chartered member of the CSQA.</li>
      <li>Maintains the Appropriate Professional Indemnity Insurance.</li>
      <li>is registered with the Tax Practitioners Board. All quantity surveyors who prepare Property Tax Depreciation Schedules are required by the ATO to be registered with the Tax Practitioners Board which checks that the person preparing the reports is suitably qualified and maintains the appropriate professional indemnity insurance. You can check the registration on the TPB website. Our registration number is 31774026.</li>
    </ul>
  </article>

  <article class="card" style="left:355px;top:82px;width:150px;height:190px">
    <h2>Is my property<br>too old?</h2>
    <p>No, if your property was constructed after 1990 you can claim for both the construction cost element and the Plant and equipment. If it was built before then you can still claim the plant and equipment allowance. The easiest thing to do is to contact us with some details on your property and we can make an initial assessment of the possible annual savings.</p>
  </article>

  <article class="card" style="left:355px;top:277px;width:150px;height:235px">
    <h2>My property<br>is in Ireland does<br>this make<br>a difference?</h2>
    <p>Division 43 of the Income Tax Assessment Act 1997 which deals with capital works depreciation states that it applies to buildings begun outside Australia after 21 August 1990 Sect 43.20 (1) (b). Your Australian tax return should cover your worldwide income. As long as the property is available to rent back in Ireland you are obliged by the ATO to report any income or loss on that property.</p>
  </article>

  <article class="card" style="left:22px;top:397px;width:326px;height:113px">
    <h2>What is Property Depreciation?</h2>
    <p>Just like you claim wear and tear on a car purchased for income producing purposes, you can also claim the depreciation of your investment property against your taxable income.<br>There are 2 types available: depreciation on Plant and Equipment, and depreciation on the cost of construction. Plant and Equipment refers to items within the building like ovens, dishwashers, carpet and blinds etc. Both these costs can be offset against your assessable income.</p>
  </article>

  <article class="card" style="left:22px;top:517px;width:240px;height:133px">
    <h2>How much will<br>the report cost?</h2>
    <p>Each scenario is different so contact us to obtain a quick quote for your situation. Generally the cost of the report is a fraction of the savings in any one year.</p>
    <ul class="ticks">
      <li>Our fee is fully tax deductible</li>
      <li>You do NOT need to get this report done every year so the cost can be spread over several years</li>
    </ul>
  </article>

  <article class="card" style="left:268px;top:517px;width:237px;height:133px">
    <h2>I haven't included my property for the past couple of years on my tax return is this a problem?</h2>
    <p>No, in actual fact you could have been missing out on savings for a number of years, you can also use this report to claim a refund from the ATO for up to the past three years.</p>
  </article>

  <div class="band-bottom"></div>
  <div class="partner"><span class="partner-mark"></span>CSQA</div>
  <div class="badge" role="img" aria-label="Registration badge"></div>
</section>

<section class="page page--example">
  <div class="band-top"></div>
  <div class="band-top-line"></div>
  <div class="example-title">Property Tax Depreciation Example<br>3 bed Semi - detached house<br>Dublin, Constructed in 2006</div>

  <div class="sheet">
    <table>
      <colgroup>
        <col class="c-ref"><col class="c-desc"><col class="c-note"><col class="c-eur"><col class="c-aud"><col class="c-with">
      </colgroup>
      <thead>
        <tr><th class="ref" rowspan="2">Ref</th><th rowspan="2">Description</th><th rowspan="2"></th><th class="eur" colspan="2" style="height:36px">Without Property<br>Tax Depreciation</th><th class="with">With Property<br>DepreciationReport</th></tr>
        <tr><th class="eur">Euro</th><th class="aud">AUD</th><th class="with">AUD</th></tr>
      </thead>
      <tbody>
        <tr class="group"><td class="ref" style="height:34px">A</td><td>Rental Income</td><td class="note">€1,200 &nbsp; Month</td><td class="eur">€14,400</td><td class="aud">$20,571</td><td class="with">$20,571</td></tr>
      </tbody>
      <tbody>
        <tr class="group"><td class="ref"></td><td>Expenses</td><td class="note"></td><td class="eur"></td><td class="aud"></td><td class="with"></td></tr>
        <tr><td class="ref">B</td><td colspan="2">Annual Interest charged on<br>outstanding Mortgage (4% apr)</td><td class="eur">€12,040</td><td class="aud">$17,200</td><td class="with">$17,200</td></tr>
        <tr><td class="ref">C</td><td colspan="2">Property agent fees or commission</td><td class="eur">€1,200</td><td class="aud">$1,714</td><td class="with">$1,714</td></tr>
        <tr><td class="ref">D</td><td>Local Property Tax</td><td class="note"></td><td class="eur">€250</td><td class="aud">$357</td><td class="with">$357</td></tr>
        <tr><td class="ref">E</td><td>Repairs and Maintenance</td><td class="note"></td><td class="eur">€2,000</td><td class="aud">$2,857</td><td class="with">$2,857</td></tr>
        <tr><td class="ref">F</td><td>Home Insurance</td><td class="note"></td><td class="eur">€450</td><td class="aud">$643</td><td class="with">$643</td></tr>
        <tr><td class="ref">G</td><td>Cleaning Advertising et..</td><td class="note"></td><td class="eur">€1,500</td><td class="aud">$2,143</td><td class="with">$2,143</td></tr>
        <tr class="green-text"><td class="ref">H</td><td>Property Tax Depreciation</td><td class="note"></td><td class="eur">€0</td><td class="aud">$0</td><td class="with green-val">$15,000</td></tr>
        <tr class="sub"><td class="ref">I</td><td>Total Annual &nbsp;Expenses</td><td class="note">Total (B to H)</td><td class="eur">€17,440</td><td class="aud">$24,914</td><td class="with">$39,914</td></tr>
        <tr class="sub"><td class="ref">J</td><td>Annual Rental Loss/Gain</td><td class="note">(A less I)</td><td class="eur">€3,040</td><td class="aud">$4,343</td><td class="with">$19,343</td></tr>
      </tbody>
      <tbody>
        <tr class="group"><td class="ref" style="height:34px">K</td><td>Your Annual Income from other<br>sources</td><td class="note"></td><td class="eur"></td><td class="aud">$180,000</td><td class="with">$180,000</td></tr>
        <tr><td class="ref" style="height:34px">L</td><td>Tour Taxable Income after Rental<br>Losses/Gains</td><td class="note">(K Plus J)</td><td class="eur"></td><td class="aud">$175,657</td><td class="with">$160,657</td></tr>
      </tbody>
      <tbody>
        <tr class="group"><td class="ref">N</td><td>Annual Tax Saving</td><td class="note">(J multiplied by M)</td><td class="eur"></td><td class="aud">$1,694</td><td class="with">$7,544</td></tr>
        <tr><td class="ref"></td><td>Foreign Tax Credits</td><td class="note"></td><td class="eur"></td><td class="aud"></td><td class="with"></td></tr>
        <tr><td class="ref">O</td><td>Non-resident Landlord withholding<br>Tax (20% Ireland)</td><td class="note">(A multiplied by 20%)</td><td class="eur">€2,880</td><td class="aud">$4,114</td><td class="with">$4,114</td></tr>
        <tr><td class="ref">P</td><td>Nett Tax Savings</td><td class="note">(N Plus O)</td><td class="eur"></td><td class="aud">$5,808</td><td class="with">$11,658</td></tr>
      </tbody>
      <tbody>
        <tr class="group"><td class="ref" style="height:52px">Q</td><td>Additional Money in your Pocket<br>(Australia) per year due to<br>Property Tax Depreciation</td><td class="note"></td><td class="eur"></td><td class="aud"></td><td class="with">$5,850</td></tr>
      </tbody>
    </table>
  </div>

  <div class="band-bottom"></div>
  <div class="brand"><span class="brand-dot"></span>Tolbexmu Depreciation</div>
</section>

</body>
</html>
```